依頼詳細
色の指定はありませんが、円満相続をイメージさせる明るい色を希望します。
お客様へのわかりやすさ、相談したいなと思わせるイメージです。
記載項目
表面:氏名/森岡達彦(モリオカタツヒコ)会社名/有限会社ミナレスト 役職/代表取締役 資格/不動産賃貸経営管理士・宅地建物取引主任者・相続士・NPO法人継承くらし支援ネット会員
住所/〒798-0417愛媛県宇和島市柳川町3丁目4-2 電話/0895-41-7782 Fax/0895-41-7783 携帯/090-5827-1146 Mail/morioka@minarest-ex.jp http://www.minarest-ex.jp

裏面:社是・・・創動継志       創造・行動・継続   習
(※添付しているロゴ使用)    志       慣
※志を分母、創造・行動・継続を分子、上に線を入れられなかったので文字で説明しまし
た。上記を習慣にしていくという意味です。

理念・・・志事(シゴト)を通じ、物心両面の幸福を追求し、自らが創造成長することで、
縁ある大事な方々に、喜んでもらえることを使命とします。

※上記に「相続を受ける人によって様々な方法や対策があります。自身の相続や不動産業・生   保・損保代理店の経験に基づいたお客様にとって最善な方法をご提案します。」みたいなわか
りやすい説明をいれて欲しいです。

希望イメージ
シンプル 複雑
単色 カラフル
暗い 明るい
日常 高級
遊び心 厳粛
未来的 伝統的
女性的 男性的
希望する色
納品ファイル
• 高解像度JPG (.jpg)
• イラストレーター形式 (.ai)
補足説明
依頼公開後の追記内容

明るく、もらった方に安心感を与えられるような点

貴重なお時間をいただき、また素敵なご提案をいただきましてありがとうございました。

```html
<!DOCTYPE html>
<html lang="ja">
<head>
<meta charset="utf-8">
<title>有限会社ミナレスト 森岡達彦 名刺</title>
<link rel="stylesheet" href="https://fonts.googleapis.com/css2?family=Noto+Sans+JP:wght@300;400;500&display=swap">
<style>
  :root {
    --paper: #ffffff;
    --ink: #3c3c3c;
    --ink-strong: #222222;
    --ink-soft: #555555;
    --band-grey: #dcdedb;
    --band-green: #5f9f7f;
    --tone-a: #f3f3f1;
    --tone-b: #e6ecd8;
    --tone-c: #d8e6ef;
    --tone-d: #f3e2cf;
  }
  * { margin: 0; padding: 0; box-sizing: border-box; }
  html, body { width: 805px; height: 1200px; overflow: hidden; background: var(--paper); }
  body { font-family: "Noto Sans JP", sans-serif; color: var(--ink); }

  .card { position: relative; width: 805px; height: 1200px; background: var(--paper); }

  .hero-illustration {
    position: absolute; left: 215px; top: 148px; width: 402px; height: 415px;
  }

  .company { position: absolute; left: 134px; top: 566px; font-size: 25px; font-weight: 400; letter-spacing: 0.02em; }
  .role { position: absolute; left: 134px; top: 636px; font-size: 22px; }
  .name-row { position: absolute; left: 134px; top: 680px; display: flex; align-items: baseline; gap: 18px; }
  .name { font-size: 46px; font-weight: 400; color: var(--ink-strong); letter-spacing: 0.04em; }
  .name-roman { font-size: 22px; font-weight: 300; color: var(--ink-soft); }

  .credentials { position: absolute; left: 134px; top: 762px; font-size: 20px; line-height: 32px; }
  .contact { position: absolute; left: 134px; top: 858px; font-size: 21px; line-height: 35px; list-style: none; }

  .band-grey { position: absolute; left: 0; top: 1094px; width: 805px; height: 34px; background: var(--band-grey); }
  .band-green { position: absolute; left: 0; top: 1128px; width: 805px; height: 72px; background: var(--band-green); }
</style>
</head>
<body>
<main class="card">
  <svg class="hero-illustration" viewBox="0 0 402 415" role="img" aria-label="パステルカラーのパズルピースで組み上げた家のイラスト">
    <defs>
      <linearGradient id="houseTone" x1="0" y1="0" x2="1" y2="1">
        <stop offset="0" stop-color="var(--tone-b)"/>
        <stop offset="0.45" stop-color="var(--tone-a)"/>
        <stop offset="0.75" stop-color="var(--tone-c)"/>
        <stop offset="1" stop-color="var(--tone-d)"/>
      </linearGradient>
    </defs>
    <rect x="0" y="0" width="402" height="415" rx="14" fill="url(#houseTone)"/>
  </svg>

  <p class="company">有限会社ミナレスト</p>
  <p class="role">代表取締役</p>
  <div class="name-row">
    <h1 class="name">森岡 達彦</h1>
    <span class="name-roman">Tatsuhiko Morioka</span>
  </div>

  <div class="credentials">
    <p>資格：</p>
    <p>不動産賃貸経営管理士・宅地建物取引主任者・</p>
    <p>相続士・NPO 法人継承くらし支援ネット会員</p>
  </div>

  <ul class="contact">
    <li>〒798-0417 愛媛県宇和島市柳川町3丁目4-2</li>
    <li>TEL. 0895-41-7782　FAX. 0895-41-7783</li>
    <li>携帯. 090-5827-1146</li>
    <li>Mail : morioka@minarest-ex.jp</li>
    <li>URL : http://www.minarest-ex.jp</li>
  </ul>

  <div class="band-grey"></div>
  <div class="band-green"></div>
</main>
</body>
</html>
```